Vantrel Web Services

This is a new It services company operating in Perth western Australia

we need a website that is easy to navigate without a cluttered feel to it it should have the following links and pages

About Us
Services
Clients
Contact Us
MY Vantrel (login for clients)

Hi it is a web based IT services company so we would expect customers to come to the website for 2 different purposes the first is to enquire about our services and then as they become customers come to our website to manage their services so whilst they are seperate we want do not want it to look like 2 different websites

hope this helps

Hi to update this we need a home page and templates for sub pages

this is a design brief only and not the coding of the pages or building of the site

```html
<!DOCTYPE html>
<html lang="en">
<head>
<meta charset="utf-8">
<title>Vantrel Web Services</title>
<link href="https://fonts.googleapis.com/css2?family=Open+Sans:wght@400;600;700&display=swap" rel="stylesheet">
<style>
:root{
  --cyan:#1bb8e8;
  --logo-bg:#c3ebf8;
  --navy:#1d2b6b;
  --brand-red:#d0161d;
  --btn-red:#c8161d;
  --btn-red-dark:#8e0d12;
  --nav-active:#1f1f1f;
  --ink:#2e2e2e;
  --muted:#9a9a9a;
  --white:#ffffff;
  --footer:#333335;
  --footer-bottom:#222224;
  --footer-text:#d5d5d5;
  --blue-btn:#1c6fae;
}
*{margin:0;padding:0;box-sizing:border-box}
html,body{width:1200px;height:2699px;overflow:hidden}
body{position:relative;font-family:"Open Sans",Arial,sans-serif;color:var(--ink);background:var(--white)}

/* header */
.site-header{position:absolute;left:0;top:0;width:1200px;height:104px;background:var(--cyan)}
.brand{position:absolute;left:111px;top:0;width:369px;height:104px;background:var(--logo-bg);display:flex;align-items:center;padding-left:22px;gap:18px}
.brand-dot{width:66px;height:66px;border-radius:50%;background:var(--brand-red)}
.brand-name{font-weight:700;font-size:38px;color:var(--navy);letter-spacing:1px}
.toll{position:absolute;right:110px;top:15px;font-size:15px;color:#0d5d7e}
.toll strong{color:var(--white);font-weight:700}
.main-nav{position:absolute;top:54px;right:106px;height:50px;display:flex}
.main-nav a{display:block;height:50px;line-height:50px;color:var(--white);text-decoration:none;font-size:15px;font-weight:600;padding:0 15px;white-space:nowrap}
.main-nav a.active{background:var(--nav-active);padding:0 12px;margin-right:10px}

/* hero */
.hero{position:absolute;left:0;top:104px;width:1200px;height:457px;background:linear-gradient(180deg,#2b2b2b,#1f1f1f)}
.hero-title{position:absolute;left:0;top:105px;width:1200px;text-align:center;color:var(--white);font-weight:600;font-size:37px;line-height:52px}
.hero-form{position:absolute;top:236px;left:311px;display:flex;gap:11px}
.hero-input{width:419px;height:45px;background:#111;border-radius:3px;color:#777;font-style:italic;font-size:13px;line-height:45px;padding-left:18px}
.btn-red{background:var(--btn-red);border:2px solid var(--btn-red-dark);border-radius:3px;color:var(--white);font-weight:600;text-align:center}
.hero-btn{width:148px;height:45px;line-height:41px;font-size:17px}

/* desk scene */
.desk-band{position:absolute;left:0;top:561px;width:1200px;height:452px;background:linear-gradient(180deg,#e9e9e9,#d9d9d9)}
.desk-laptop{position:absolute;left:283px;top:500px;width:635px;height:468px;border-radius:22px 22px 12px 12px;background:linear-gradient(180deg,#3a3a3a 0,#3a3a3a 28%,#f4f4f4 28%,#e6e6e6 100%)}

/* services */
.services{position:absolute;left:0;top:1013px;width:1200px;height:777px;background:linear-gradient(180deg,#f2f2f2,#e9e9e9)}
.section-title{position:absolute;left:0;width:1200px;text-align:center;font-size:29px;font-weight:400;color:#333}
.section-lead{position:absolute;left:100px;width:1000px;text-align:center;font-size:14px;line-height:24px;color:#666}
.service{position:absolute;width:320px;text-align:center}
.service svg{display:block;margin:0 auto;width:52px;height:52px}
.service h3{font-weight:400;font-size:20px;color:#333;margin-top:6px}
.service p{font-size:14px;line-height:24px;color:var(--muted);margin-top:10px}

/* features */
.enroll-btn{position:absolute;left:477px;top:1990px;width:248px;height:46px;line-height:42px;font-size:17px}
.feature{position:absolute;top:2081px;width:302px}
.feature-img{width:302px;height:196px}
.feature h4{font-size:15px;font-weight:700;color:#333;margin-top:16px;text-transform:uppercase}
.feature p{font-size:13px;line-height:24px;color:var(--muted);margin-top:8px}

/* footer */
.site-footer{position:absolute;left:0;top:2450px;width:1200px;height:191px;background:var(--footer)}
.join{position:absolute;left:111px;top:62px;font-size:15px;color:var(--footer-text)}
.foot-form{position:absolute;left:111px;top:90px;display:flex;gap:13px}
.foot-input{width:432px;height:33px;background:var(--white);color:#999;font-size:16px;line-height:33px;padding-left:8px}
.foot-btn{width:108px;height:33px;line-height:33px;background:var(--blue-btn);color:var(--white);font-weight:700;font-size:14px;text-align:center}
.socials{position:absolute;left:790px;top:80px;display:flex;gap:30px}
.socials svg{width:38px;height:38px}
.bottom-bar{position:absolute;left:0;top:2641px;width:1200px;height:58px;background:var(--footer-bottom);font-size:13px;color:#aaa}
.bottom-bar .copy{position:absolute;left:111px;top:19px}
.bottom-bar .legal{position:absolute;right:110px;top:19px}
</style>
</head>
<body>

<header class="site-header">
  <div class="brand"><span class="brand-dot"></span><span class="brand-name">Vantrel</span></div>
  <div class="toll">Call Toll Free: <strong>0800-555-0199</strong></div>
  <nav class="main-nav">
    <a class="active" href="#">Home</a>
    <a href="#">About Us</a>
    <a href="#">Services</a>
    <a href="#">Clients</a>
    <a href="#">Contact Us</a>
    <a href="#">MY Vantrel</a>
  </nav>
</header>

<section class="hero" role="img" aria-label="Dark photograph of an office workspace">
  <h1 class="hero-title">Welcome To The VANTREL<br>Newely Founded Online Media &amp; IT-Services</h1>
  <div class="hero-form">
    <div class="hero-input">Enter Your Email Address...</div>
    <div class="btn-red hero-btn">Get Subcribe</div>
  </div>
</section>

<div class="desk-band" role="img" aria-label="Illustration of a desk with calendar, pen, documents and address book"></div>
<div class="desk-laptop" role="img" aria-label="Illustration of an open laptop seen from above"></div>

<section class="services">
  <h2 class="section-title" style="top:62px">We Do IT-Services</h2>
  <p class="section-lead" style="top:120px">Lorem ipsum dolor sit amet, consectetur adipisicing elit, sed do eiusmod tempor incididunt ut labore et dolore magna aliqua.<br>Ut enim ad minim veniam, quis nostrud exercitation ullamco laboris nisi ut aliquip ex ea commodo consequat. Duis aute<br>irure dolor in reprehenderit in voluptate velit esse cillum dolore eu fugiat nulla pariatur.</p>

  <div class="service" style="left:104px;top:275px">
    <svg viewBox="0 0 52 52"><rect x="5" y="8" width="42" height="28" rx="2" fill="none" stroke="#1a8fd0" stroke-width="3"/><path d="M17 22l6 6 12-12" fill="none" stroke="#1a8fd0" stroke-width="3"/><rect x="18" y="40" width="16" height="3" fill="#1a8fd0"/></svg>
    <h3>System Administration</h3>
    <p>Lorem ipsum dolor sit amet, consectetur adip-isicing elit, sed do eiusmod tempor incididunt ut labore dolor magna aliqua.</p>
  </div>
  <div class="service" style="left:440px;top:275px">
    <svg viewBox="0 0 52 52"><rect x="8" y="6" width="30" height="11" rx="2" fill="#2ab24a"/><rect x="8" y="20" width="30" height="11" rx="2" fill="#2ab24a"/><rect x="8" y="34" width="22" height="11" rx="2" fill="#2ab24a"/><circle cx="40" cy="40" r="8" fill="none" stroke="#2ab24a" stroke-width="3"/></svg>
    <h3>Database Administration</h3>
    <p>Lorem ipsum dolor sit amet, consectetur adip-isicing elit, sed do eiusmod tempor incididunt ut labore dolor magna aliqua.</p>
  </div>
  <div class="service" style="left:776px;top:275px">
    <svg viewBox="0 0 52 52"><rect x="6" y="10" width="40" height="26" rx="2" fill="none" stroke="#2bb5a0" stroke-width="2.5"/><path d="M20 18l-5 5 5 5M32 18l5 5-5 5M28 16l-4 14" fill="none" stroke="#2bb5a0" stroke-width="2.5"/><rect x="2" y="38" width="48" height="4" fill="#2bb5a0"/></svg>
    <h3>Programming</h3>
    <p>Lorem ipsum dolor sit amet, consectetur adip-isicing elit, sed do eiusmod tempor incididunt ut labore dolor magna aliqua.</p>
  </div>

  <div class="service" style="left:104px;top:505px">
    <svg viewBox="0 0 52 52"><circle cx="32" cy="16" r="11" fill="none" stroke="#e2473c" stroke-width="3"/><path d="M32 10v12" stroke="#e2473c" stroke-width="3"/><path d="M10 30h10l6 6v10H14z" fill="#e2473c"/></svg>
    <h3>Database &amp; Query Tuning</h3>
    <p>Lorem ipsum dolor sit amet, consectetur adip-isicing elit, sed do eiusmod tempor incididunt ut labore dolor magna aliqua.</p>
  </div>
  <div class="service" style="left:440px;top:505px">
    <svg viewBox="0 0 52 52"><rect x="10" y="4" width="32" height="44" rx="3" fill="#1fa5dc"/><path d="M30 4v16l4-3 4 3V4" fill="#0c6f99"/></svg>
    <h3>Content Services</h3>
    <p>Lorem ipsum dolor sit amet, consectetur adip-isicing elit, sed do eiusmod tempor incididunt ut labore dolor magna aliqua.</p>
  </div>
  <div class="service" style="left:776px;top:505px">
    <svg viewBox="0 0 52 52"><circle cx="26" cy="26" r="6" fill="#8a4fa8"/><circle cx="10" cy="30" r="5" fill="#8a4fa8"/><circle cx="40" cy="10" r="5" fill="#8a4fa8"/><circle cx="42" cy="40" r="5" fill="#8a4fa8"/><path d="M10 30L26 26 40 10M26 26L42 40" stroke="#8a4fa8" stroke-width="3"/></svg>
    <h3>Social Media Marketing</h3>
    <p>Lorem ipsum dolor sit amet, consectetur adip-isicing elit, sed do eiusmod tempor incididunt ut labore dolor magna aliqua.</p>
  </div>
</section>

<h2 class="section-title" style="top:1835px">Sed Do Euismod Tempor Incidunt Magna Aliqua</h2>
<p class="section-lead" style="top:1892px">Lorem ipsum dolor sit amet, consectetur adipisicing elit, sed do eiusmod tempor incididunt ut labore et dolore magna aliqua.<br>Ut enim ad minim veniam, quis nostrud exercitation ullamco laboris nisi ut aliquip ex ea commodo consequat. Duis aute<br>irure dolor in reprehenderit in voluptate velit esse cillum dolore eu fugiat nulla pariatur.</p>
<div class="btn-red enroll-btn">Click Here To Enroll Now</div>

<article class="feature" style="left:110px">
  <div class="feature-img" role="img" aria-label="Photo of laptop, tablet and phone devices" style="background:linear-gradient(135deg,#f4f4f4,#cfd6df);border:1px solid #ddd"></div>
  <h4>Lorem ipsum dolor sit amet</h4>
  <p>Lorem ipsum dolor sit amet, consectetur adipsi-cing elit, sed do eiusmod tempor incididunt ut labore dolor magna aliqua.</p>
</article>
<article class="feature" style="left:450px">
  <div class="feature-img" role="img" aria-label="Photo of program code on a screen" style="background:linear-gradient(135deg,#16304d,#2b5c86)"></div>
  <h4>Lorem ipsum dolor sit amet</h4>
  <p>Lorem ipsum dolor sit amet, consectetur adipsi-cing elit, sed do eiusmod tempor incididunt ut labore dolor magna aliqua.</p>
</article>
<article class="feature" style="left:790px">
  <div class="feature-img" role="img" aria-label="Photo of a tablet on a wooden desk" style="background:linear-gradient(135deg,#7a4a2a,#3c2414)"></div>
  <h4>Lorem ipsum dolor sit amet</h4>
  <p>Lorem ipsum dolor sit amet, consectetur adipsi-cing elit, sed do eiusmod tempor incididunt ut labore dolor magna aliqua.</p>
</article>

<footer class="site-footer">
  <p class="join">Join 8,000 Smart Owners Who Get Our Emails Every Month. Be Better In 2014.</p>
  <div class="foot-form">
    <div class="foot-input">name@example.com</div>
    <div class="foot-btn">SUBCRIBE</div>
  </div>
  <div class="socials">
    <svg viewBox="0 0 38 38"><rect x="11" y="3" width="16" height="32" rx="3" fill="none" stroke="#fff" stroke-width="3"/><circle cx="19" cy="30" r="1.8" fill="#fff"/></svg>
    <svg viewBox="0 0 38 38"><circle cx="19" cy="19" r="15" fill="none" stroke="#fff" stroke-width="3"/></svg>
    <svg viewBox="0 0 38 38"><rect x="4" y="4" width="30" height="30" rx="3" fill="none" stroke="#fff" stroke-width="3"/></svg>
    <svg viewBox="0 0 38 38"><circle cx="19" cy="19" r="15" fill="none" stroke="#fff" stroke-width="3"/></svg>
    <svg viewBox="0 0 38 38"><rect x="4" y="6" width="30" height="26" fill="none" stroke="#fff" stroke-width="3"/><path d="M4 6l15 14L34 6M4 32l12-12M34 32L22 20" fill="none" stroke="#fff" stroke-width="2.5"/></svg>
  </div>
</footer>
<div class="bottom-bar">
  <span class="copy">Copyrights © 2014 Vantrel.com - All Rights Reserved</span>
  <span class="legal">Privacy Policy &nbsp;&nbsp;|&nbsp;&nbsp; Term &amp; Conditions</span>
</div>

</body>
</html>
```